Pool Builder Website Design in arizona

Our current site is located here: kelvaro.net

We are looking to give this a modern facelift. We will be cutting your design into a wordpress theme so we can utilize the CMS plateform backend.

Look and Feel
• Clean cut and professional
• Mobile friendly
• Updated from old site
• Feel intrigued but relax (do you have trust logos? Marla looking into this)
Colors
• Warm tropical neutral colors
• Orange, brown, blues
- Please make the site modern and more sleek look that looks like a 2015 style design and NOT 1999.
- Must be coded as a wordpress theme
- must create a home page, inner page and blog page
- must allow client to BLOG using the post section in wordpress

This pool company is a pool builder/installer in Phoenix arizona.

NOTE::: Please create a home page and one internal page.

Serif
Sans Serif

• - Must be coded as a wordpress theme
• - must create a home page, inner page and blog page
• - must allow client to BLOG using the post section in wordpress

```html
<!DOCTYPE html>
<html lang="en">
<head>
<meta charset="utf-8">
<title>Kelvaro Pools — Pool Builder/Installer in Phoenix Arizona</title>
<link rel="stylesheet" href="https://fonts.googleapis.com/css2?family=Montserrat:wght@400;500&family=Roboto:wght@400&display=swap">
<style>
:root{
  --blue:#1a9ad6;
  --blue-dark:#0a78b8;
  --green:#6fb52c;
  --ink:#1e1e1e;
  --text:#555;
  --footer-bg:#ededed;
  --water-light:#c9dcea;
  --water-deep:#1668b4;
}
*{box-sizing:border-box;margin:0;padding:0}
html,body{width:908px;height:1200px;overflow:hidden}
body{position:relative;background:#fff;font-family:"Roboto",Arial,sans-serif;color:var(--text)}
.site-header{position:absolute;left:0;top:0;width:908px;height:91px;background:#fff;border-bottom:1px solid #dde5ec}
.brand{position:absolute;left:84px;top:24px;display:flex;align-items:center;gap:8px;font-family:"Montserrat",sans-serif;font-weight:500;font-size:21px;color:var(--blue-dark)}
.brand-dot{width:26px;height:26px;border-radius:50%;background:var(--green)}
.call-now{position:absolute;right:84px;top:51px;font-family:"Montserrat",sans-serif;font-size:12px;color:var(--ink);display:flex;align-items:center;gap:4px}
.water{position:absolute;left:0;top:91px;width:908px;height:1065px;background:linear-gradient(180deg,var(--water-light) 0%,#8fb6d8 25%,#3f8ccb 60%,var(--water-deep) 100%)}
.page{position:absolute;left:65px;top:104px;width:778px;height:1038px;background:#fff;box-shadow:0 2px 8px rgba(0,0,0,.25)}
.main-nav{display:flex;height:49px;background:linear-gradient(180deg,#2aa6e0,#0b83c4)}
.main-nav a{display:flex;align-items:center;justify-content:center;color:#fff;text-decoration:none;font-family:"Montserrat",sans-serif;font-size:9.5px;border-right:1px solid rgba(0,0,0,.12)}
.main-nav a.active{background:linear-gradient(180deg,#7cc23a,#5a9e22)}
.hero{position:relative;height:359px;background:linear-gradient(160deg,#b08a72 0%,#9aa3ad 22%,#1f7fd6 45%,#0d5fc8 70%,#b9826a 100%)}
.hero-caption{position:absolute;left:19px;top:205px;width:539px;height:120px;background:rgba(30,160,225,.82);padding:24px 21px;color:#fff}
.hero-caption h1{font-family:"Montserrat",sans-serif;font-weight:400;font-size:19px;letter-spacing:.2px}
.hero-caption p{font-family:"Montserrat",sans-serif;font-size:9px;line-height:15.5px;margin-top:6px;width:480px}
.dots{display:flex;gap:6px;margin-top:12px}
.dots span{width:7px;height:7px;border-radius:50%;background:rgba(255,255,255,.45)}
.dots span.on{background:#fff}
.welcome{text-align:center;padding:27px 21px 0}
.welcome h2{font-family:"Montserrat",sans-serif;font-weight:400;font-size:16px;color:var(--ink)}
.welcome h2 span,.feature h3 span{color:var(--blue)}
.welcome h3{font-family:"Montserrat",sans-serif;font-weight:400;font-size:11px;color:var(--green);margin-top:6px}
.welcome p{font-size:8.6px;line-height:19.4px;margin-top:7px}
.btn{display:inline-flex;align-items:center;justify-content:center;background:linear-gradient(180deg,#1fa0dc,#0b7fc1);color:#fff;font-family:"Montserrat",sans-serif;font-size:8.5px;text-decoration:none;border-radius:2px}
.btn-quote{width:144px;height:37px;margin-top:14px}
.features{position:absolute;left:19px;top:646px;width:740px;display:flex;justify-content:space-between}
.feature{width:360px}
.feature h3{font-family:"Montserrat",sans-serif;font-weight:400;font-size:15px;color:var(--ink)}
.feature-photo{height:144px;margin-top:11px}
.photo-building{background:linear-gradient(170deg,#2b2a22 0%,#3c3a2e 35%,#5fd0e0 55%,#9c8a7c 85%)}
.photo-install{background:linear-gradient(170deg,#4a4038 0%,#5a4c44 35%,#1c5ab0 60%,#a08878 90%)}
.feature p{font-size:8.6px;line-height:19.4px;margin-top:12px}
.btn-more{width:107px;height:36px;margin-top:13px}
.site-info{position:absolute;left:0;top:975px;width:778px;height:63px;background:var(--footer-bg);display:flex;align-items:center;padding:0 19px;font-size:8.6px;color:#555;gap:20px}
.site-info .item{display:flex;align-items:center;gap:5px;white-space:nowrap}
.social{display:flex;gap:4px;margin-left:auto}
.social span{width:21px;height:21px;border-radius:50%}
.bottom-bar{position:absolute;left:84px;right:84px;top:1172px;display:flex;justify-content:space-between;font-size:8px;color:#666}
</style>
</head>
<body>
<header class="site-header">
  <div class="brand"><span class="brand-dot"></span>Kelvaro Pools</div>
  <div class="call-now">
    <svg width="10" height="10" viewBox="0 0 10 10"><rect width="10" height="10" rx="2" fill="#0a78b8"/><path d="M3 2.5c.4 2 1.8 3.6 4.2 4.6l.6-1-1.2-.6-.5.5C5.3 5.5 4.7 4.9 4.3 4.1l.5-.5-.6-1.2z" fill="#fff"/></svg>
    CALL NOW! 480-555-0142
  </div>
</header>

<div class="water" role="img" aria-label="Blurred pool water background"></div>

<div class="page">
  <nav class="main-nav">
    <a class="active" style="width:114px">HOME</a>
    <a style="width:113px">STYLES</a>
    <a style="width:133px">PORTFOLIO</a>
    <a style="width:146px">INSTALLATION</a>
    <a style="width:128px">ABOUT US</a>
    <a style="width:144px;border-right:0">CONTACT US</a>
  </nav>

  <section class="hero" role="img" aria-label="Photo of a fiberglass pool with spa on a brick paver patio">
    <div class="hero-caption">
      <h1>POOL BUILDER/INSTALLER IN PHOENIX ARIZONA</h1>
      <p>Lorem ipsum dolor sit amet, consectetuer adipiscing elit, sed diam nonummy nibh euismod tincidunt ut laoreet dolore magna aliquam erat volutpat.</p>
      <div class="dots"><span></span><span class="on"></span><span></span><span></span></div>
    </div>
  </section>

  <section class="welcome">
    <h2>WELCOME TO <span>KELVARO POOLS</span></h2>
    <h3>THE FIBERGLASS POOL EXPERTS!</h3>
    <p>A Phoenix fiberglass pool is more than just a relaxing piece of heaven, it is an investment. &nbsp;Why spend your money on a pool that requires more maintenance and scratches your feet when you can enjoy the smooth feeling of fiberglass on your toes? &nbsp;Fiberglass pools offer many unique advantages over concrete pools, and Kelvaro Pools are the premier AZ fiberglass pool builders. &nbsp;&nbsp;We also offer many other products and services to enhance your yard and increase the value of your home. Check out some of our cost effective and sensuous fiberglass spools and spas, our beautiful and calming custom water features, or our fun custom beehives, firepits, and barbecues. &nbsp;Our fiberglass pools come in many sizes and styles and installation is a breeze. &nbsp;Call or stop in today to see how we can make your yard "A small bit of paradise"! We are the best arizona pool builder.</p>
    <a class="btn btn-quote">GET QUOTE NOW !</a>
  </section>

  <section class="features">
    <article class="feature">
      <h3>POOL <span>BUILDING</span></h3>
      <div class="feature-photo photo-building" role="img" aria-label="Photo of a freeform turquoise fiberglass pool at dusk"></div>
      <p>Lorem ipsum dolor sit amet, consectetuer adipiscing elit, sed diam nonummy nibh euismod tincidunt ut laoreet dolore magna aliquam erat volutpat. Ut wisi enim ad minim veniam, quis nostrud exerci tation ullamcorper suscipit lobortis nisl ut aliquip ex ea commodo consequat.</p>
      <a class="btn btn-more">READ MORE</a>
    </article>
    <article class="feature">
      <h3>POOL <span>INSTALLATION</span></h3>
      <div class="feature-photo photo-install" role="img" aria-label="Photo of a blue pool with a rock waterfall feature"></div>
      <p>Duis autem vel eum iriure dolor in hendrerit in vulputate velit esse molestie consequat, vel illum dolore eu feugiat nulla facilisis at vero eros et accumsan et iusto odio dignissim qui blandit praesent luptatum zzril delenit augue duis dolore te feugait nulla facilisi. Nam liber tempor cum soluta nobis eleifend.</p>
      <a class="btn btn-more">READ MORE</a>
    </article>
  </section>

  <footer class="site-info">
    <div class="item"><svg width="7" height="11" viewBox="0 0 7 11"><path d="M3.5 0A3.5 3.5 0 0 0 0 3.5C0 6 3.5 11 3.5 11S7 6 7 3.5A3.5 3.5 0 0 0 3.5 0zm0 5a1.4 1.4 0 1 1 0-2.8 1.4 1.4 0 0 1 0 2.8z" fill="#6fb52c"/></svg>3180 W Saguaro Crest Rd. Phoenix, AZ 85029</div>
    <div class="item"><svg width="12" height="9" viewBox="0 0 12 9"><rect width="12" height="9" rx="1" fill="#6fb52c"/><path d="M1 1l5 4 5-4" stroke="#fff" fill="none"/></svg>info@kelvaro.net</div>
    <div class="item"><svg width="10" height="10" viewBox="0 0 10 10"><rect width="10" height="10" rx="2" fill="#6fb52c"/><path d="M3 2.5c.4 2 1.8 3.6 4.2 4.6l.6-1-1.2-.6-.5.5C5.3 5.5 4.7 4.9 4.3 4.1l.5-.5-.6-1.2z" fill="#fff"/></svg>480-555-0142 | Toll Free 1-877-555-0196</div>
    <div class="item"><svg width="11" height="11" viewBox="0 0 11 11"><rect x="0" y="3" width="11" height="8" rx="1" fill="#6fb52c"/><rect x="2.5" y="0" width="6" height="4" fill="#6fb52c"/><rect x="2" y="5" width="7" height="1.2" fill="#fff"/><rect x="2" y="7.5" width="7" height="1.2" fill="#fff"/></svg>480-555-0143</div>
    <div class="social">
      <span style="background:#2d4a86"></span>
      <span style="background:#f08a1c"></span>
      <span style="background:#2aa3e0"></span>
      <span style="background:#444"></span>
    </div>
  </footer>
</div>

<div class="bottom-bar">
  <span>Privacy Policy &nbsp;| &nbsp;Site Map</span>
  <span>© 2015 Kelvaro Pools. All rights reserved.</span>
</div>
</body>
</html>
```